Keynote Presentation Design Project for Crazy technology innovation company

q7venturelab is a company that do angel investments and consult/guide technology startups. In addition i have crazy innovation projects building hardware and software for fun (like tinkerpost.example). This is not a mainstream company, but has to be serious as well as innovative. Please also look at the website design here: http://q7venturelab.example

Please look at these projects for description for my logo design and website design for more information about the company.

website: (completed)
http://briefs.pixelrally.example/brief.aspx?Id=71842

logo: (completed)
http://briefs.pixelrally.example/brief.aspx?Id=86315

Target Market(s)

entrepreneurs & investors

Industry/Entity Type

Building

Requirements
Must have
• page designs:
All default keynote master slides should be styled.

page component designs/colour palettes:
tables
charts (up to 4 colors/rows)
process (a few boxes, arrows etc)

Delivery must be a keynote file and color codes in hex for all colors, and fonts must either be delivered or named.

```html
<!DOCTYPE html>
<html lang="en">
<head>
<meta charset="utf-8">
<title>q7venturelab — Keynote Master Slides</title>
<link href="https://fonts.googleapis.com/css2?family=Amatic+SC:wght@700&family=Arvo&display=swap" rel="stylesheet">
<style>
  :root {
    --stage: #ececec;
    --slide-light: #35addf;
    --slide-mid: #2696cf;
    --slide-dark: #1d83bb;
    --tab-white: #ffffff;
    --tab-shade: #d4d4d4;
    --ink-white: #ffffff;
    --ink-navy: #0e2738;
    --ink-muted: #d6eefa;
    --row-head: #3aa9e0;
    --row-a: #64b7e2;
    --row-b: #a9d6ee;
    --region-1: #1e9fe0;
    --region-2: #a6dcf5;
    --region-3: #1b86c6;
    --region-4: #145f92;
    --grid-line: rgba(255,255,255,0.25);
  }
  * { box-sizing: border-box; margin: 0; padding: 0; }
  html, body { width: 1200px; height: 1000px; overflow: hidden; background: var(--stage); }
  .stage { position: relative; width: 1200px; height: 1000px; }

  .slide {
    position: absolute;
    overflow: hidden;
    background: radial-gradient(ellipse at 50% 35%, var(--slide-light) 0%, var(--slide-mid) 55%, var(--slide-dark) 100%);
    box-shadow: 0 6px 18px rgba(0,0,0,0.25);
  }
  .slide--title { left: 130px; top: 48px; width: 930px; height: 530px; }
  .slide--table { left: 30px; top: 565px; width: 560px; height: 330px; }
  .slide--chart { left: 500px; top: 515px; width: 680px; height: 365px; }

  /* Diagonal brand tab laid across the top-left corner */
  .brand-tab {
    position: absolute;
    display: flex; align-items: center; justify-content: center; gap: 8px;
    background: linear-gradient(180deg, var(--tab-white) 55%, var(--tab-shade) 100%);
    box-shadow: 0 3px 8px rgba(0,0,0,0.3);
    font-family: "Amatic SC", cursive;
    font-weight: 700;
    color: var(--ink-navy);
    text-transform: uppercase;
    white-space: nowrap;
    transform-origin: center;
  }
  .brand-tab__mark { background: var(--region-1); flex: none; }
  .slide--title .brand-tab {
    left: -30px; top: 58px; width: 310px; height: 78px;
    font-size: 34px; transform: rotate(-27deg);
  }
  .slide--title .brand-tab__mark { width: 28px; height: 28px; }
  .slide--table .brand-tab {
    left: -30px; top: 48px; width: 220px; height: 54px;
    font-size: 24px; transform: rotate(-36deg);
  }
  .slide--chart .brand-tab {
    left: 10px; top: 44px; width: 220px; height: 54px;
    font-size: 24px; transform: rotate(-22deg);
  }
  .slide--table .brand-tab__mark,
  .slide--chart .brand-tab__mark { width: 20px; height: 20px; }

  .slide-title {
    font-family: "Amatic SC", cursive;
    font-weight: 700;
    color: var(--ink-white);
    text-transform: uppercase;
    letter-spacing: 2px;
    line-height: 1;
    white-space: nowrap;
  }
  .slide--title .slide-title {
    position: absolute; left: 0; right: 0; top: 196px;
    text-align: center; font-size: 62px;
  }
  .subhead {
    position: absolute; left: 0; right: 0; top: 278px;
    text-align: center;
    font-family: "Arvo", serif;
    font-size: 20px; line-height: 1.35;
    color: var(--ink-navy);
  }
  .slide--table .slide-title { position: absolute; left: 188px; top: 34px; font-size: 40px; }
  .slide--chart .slide-title { position: absolute; left: 230px; top: 80px; font-size: 40px; }

  .data-table {
    position: absolute; left: 118px; top: 122px;
    width: 520px;
    border-collapse: collapse;
    font-family: "Arvo", serif;
    font-size: 12px;
    color: var(--ink-navy);
  }
  .data-table th, .data-table td { text-align: left; padding: 0 18px; height: 38px; white-space: nowrap; }
  .data-table th { background: var(--row-head); color: var(--ink-white); font-weight: 400; font-size: 13px; }
  .data-table tbody tr:nth-child(odd) td { background: var(--row-a); }
  .data-table tbody tr:nth-child(even) td { background: var(--row-b); }

  .legend {
    position: absolute; left: 180px; top: 165px;
    list-style: none;
    font-family: "Arvo", serif; font-size: 11px; color: var(--ink-muted);
  }
  .legend li { display: flex; align-items: center; gap: 8px; height: 16px; }
  .legend__swatch { width: 9px; height: 9px; }

  .bar-chart { position: absolute; left: 270px; top: 140px; }
  .bar-chart text { font-family: "Arvo", serif; font-size: 8px; fill: var(--ink-muted); }
</style>
</head>
<body>
<main class="stage">

  <section class="slide slide--title">
    <div class="brand-tab"><span class="brand-tab__mark"></span>q7venturelab</div>
    <h1 class="slide-title">This is a presentation title</h1>
    <p class="subhead">This Is The Sub-Head<br>On Two Lines</p>
  </section>

  <section class="slide slide--table">
    <h2 class="slide-title">Table Slide</h2>
    <table class="data-table">
      <thead><tr><th>Header Column 1</th><th>Header Column 2</th><th>Header Column 3</th></tr></thead>
      <tbody>
        <tr><td>Lorum ispum dolor...</td><td>Lorum ispum dolor...</td><td>Lorum ispum dolor...</td></tr>
        <tr><td>Lorum ispum dolor...</td><td>Lorum ispum dolor...</td><td>Lorum ispum dolor...</td></tr>
        <tr><td>Lorum ispum dolor...</td><td>Lorum ispum dolor...</td><td>Lorum ispum dolor...</td></tr>
        <tr><td>Lorum ispum dolor...</td><td>Lorum ispum dolor...</td><td>Lorum ispum dolor...</td></tr>
      </tbody>
    </table>
    <div class="brand-tab"><span class="brand-tab__mark"></span>q7venturelab</div>
  </section>

  <section class="slide slide--chart">
    <div class="brand-tab"><span class="brand-tab__mark"></span>q7venturelab</div>
    <h2 class="slide-title">Chart Slide</h2>
    <ul class="legend">
      <li><span class="legend__swatch" style="background:var(--region-1)"></span>Region 1</li>
      <li><span class="legend__swatch" style="background:var(--region-2)"></span>Region 2</li>
      <li><span class="legend__swatch" style="background:var(--region-3)"></span>Region 3</li>
      <li><span class="legend__swatch" style="background:var(--region-4)"></span>Region 4</li>
    </ul>
    <svg class="bar-chart" width="330" height="205" viewBox="0 0 330 205" role="img" aria-label="Bar chart of four regions from 2007 to 2010">
      <g stroke="var(--grid-line)" stroke-width="1">
        <line x1="30" y1="20" x2="320" y2="20"/>
        <line x1="30" y1="60" x2="320" y2="60"/>
        <line x1="30" y1="100" x2="320" y2="100"/>
        <line x1="30" y1="140" x2="320" y2="140"/>
        <line x1="30" y1="180" x2="320" y2="180" stroke="var(--region-4)" stroke-width="2"/>
      </g>
      <text x="10" y="23">100</text><text x="14" y="63">75</text><text x="14" y="103">50</text>
      <text x="14" y="143">25</text><text x="18" y="183">0</text>
      <g>
        <rect x="38" y="148" width="16" height="32" fill="var(--region-1)"/>
        <rect x="54" y="97" width="16" height="83" fill="var(--region-2)"/>
        <rect x="70" y="142" width="16" height="38" fill="var(--region-3)"/>
        <rect x="86" y="81" width="16" height="99" fill="var(--region-4)"/>

        <rect x="108" y="151" width="16" height="29" fill="var(--region-1)"/>
        <rect x="124" y="129" width="16" height="51" fill="var(--region-2)"/>
        <rect x="140" y="90" width="16" height="90" fill="var(--region-3)"/>
        <rect x="156" y="164" width="16" height="16" fill="var(--region-4)"/>

        <rect x="178" y="122" width="16" height="58" fill="var(--region-1)"/>
        <rect x="194" y="100" width="16" height="80" fill="var(--region-2)"/>
        <rect x="210" y="164" width="16" height="16" fill="var(--region-3)"/>
        <rect x="226" y="170" width="16" height="10" fill="var(--region-4)"/>

        <rect x="248" y="68" width="16" height="112" fill="var(--region-1)"/>
        <rect x="264" y="132" width="16" height="48" fill="var(--region-2)"/>
        <rect x="280" y="116" width="16" height="64" fill="var(--region-3)"/>
        <rect x="296" y="161" width="16" height="19" fill="var(--region-4)"/>
      </g>
      <text x="58" y="196">2007</text><text x="128" y="196">2008</text>
      <text x="198" y="196">2009</text><text x="268" y="196">2010</text>
    </svg>
  </section>

</main>
</body>
</html>
```